Web Design Project

I work in a sign company that print banners, back light films, and vinyl lettering. We also create metal store signs that lights up. We have a laser cutter that can cut plastics and a waterjet that can cut stainless steel.
Job: Create a homepage
Requirements:
1. Keep it simple and neat, I do not want it to be messy. (Similar to this website, plover, or this http://www.markelvo.example/)
2. A navigation bar that has (Will help if you show a template for one of these links):
-Home
-Signs
-Banners
-Lettering
-Prints
-Gallery
3.Bottom of the page
-Abous us
-Shipping and Returning Policy
-Resellers
4.Other (Somewhere easy to find)
-Login
-Shopping Cart
-Upload
Updates
Nice job designers. I am currently working on the Site's logo, so I will be posting that up later.
I would like you guys to change the selection on the navigation bar.
It should only have:
Banners
Lettering
Prints
Gallery
Keep up the good work
Sorry for the bad update, the Navigation bar should have:
Home
Signs
Banners
Lettering
Prints
Gallery

```html
<!DOCTYPE html>
<html lang="en">
<head>
<meta charset="utf-8">
<title>Tallowmark – Banner Printing</title>
<link rel="stylesheet" href="https://fonts.googleapis.com/css2?family=Ubuntu:wght@400;500;700&family=Arimo:wght@400;700&display=swap">
<style>
:root{
  --green:#6a9a1a;
  --green-dark:#5a8612;
  --ink:#1a1a1a;
  --text:#222;
  --hero:#3c3c3c;
  --yellow:#ffee00;
  --band:#6b9b1b;
  --footer:#f5f5f5;
  --legal:#b5b5b5;
}
*{box-sizing:border-box;margin:0;padding:0}
html,body{width:915px;height:1200px;overflow:hidden;background:#fff}
body{position:relative;font-family:"Arimo",Arial,sans-serif;color:var(--text)}
a{color:inherit;text-decoration:none}
.abs{position:absolute}

.brand{left:43px;top:26px;font:500 46px/1 "Ubuntu",sans-serif;color:var(--ink);letter-spacing:.5px}
.account{right:42px;top:31px;font-size:13px;color:var(--green);display:flex;gap:7px;align-items:center}
.account svg{vertical-align:-2px}

.main-nav{left:43px;top:101px;display:flex;font:700 20px/1 "Ubuntu",sans-serif;color:var(--green)}
.main-nav a{display:flex;align-items:center;gap:3px}
.main-nav .caret{width:0;height:0;border-left:5px solid transparent;border-right:5px solid transparent;border-top:6px solid #a9a9a9;margin-left:2px}
.search{left:634px;top:97px;width:204px;height:28px;border:1px solid var(--green);border-radius:4px;padding:5px 8px;font-size:17px;color:#aaa}
.search-btn{left:847px;top:97px;width:27px;height:27px;background:var(--green);border-radius:3px;display:flex;align-items:center;justify-content:center}

.hero{left:44px;top:155px;width:830px;height:332px;background:var(--hero);border-radius:6px;overflow:hidden}
.hero-glow{left:430px;top:80px;width:620px;height:420px;border-radius:50%;background:#4a4a4a}
.hero-photo{left:13px;top:12px;width:413px;height:307px;background:linear-gradient(90deg,#e9ece8 0%,#dde3dc 35%,#7a9c3a 55%,#4f7a24 65%,#dfe4de 80%,#c9cfb8 100%)}
.burst{left:283px;top:12px}
.hero-title{left:448px;top:14px;font:500 51px/1.1 "Ubuntu",sans-serif;color:#fff;white-space:nowrap}
.hero-title span{color:var(--yellow)}
.hero-step{left:506px;font:500 29px/1 "Ubuntu",sans-serif;color:#fff;white-space:nowrap}
.browse{left:514px;top:146px;width:166px;height:40px;background:var(--green);border-radius:3px;color:#fff;font:700 28px/40px "Ubuntu",sans-serif;padding-left:16px;display:flex;align-items:center;gap:10px}
.pager{left:660px;top:298px;display:flex;gap:2px}
.pager span{width:18px;height:24px;border:1px solid #ccc;background:#8a8a8a;color:#eee;font:17px/22px "Ubuntu",sans-serif;text-align:center}
.pager span.on{background:#b0b0b0;color:#777}

.card{top:515px;width:268px;height:349px;border:1px solid #999;border-radius:7px;padding:0 16px}
.card h2{margin-top:12px;font:700 18px/1 "Arimo",sans-serif;color:#111;padding-bottom:7px;border-bottom:3px solid var(--green)}
.card .thumb{margin-top:13px;height:116px}
.card h3{margin-top:30px;font:700 13px/1.2 "Arimo",sans-serif;color:var(--green);white-space:nowrap}
.card p{margin-top:12px;font-size:13px;line-height:16.5px;color:#111}
.read-more{position:absolute;right:10px;bottom:16px;display:flex;align-items:center;gap:7px;font-size:14px;color:var(--green)}

.features{left:0;top:880px;width:915px;height:113px;background:var(--band);color:#fff}
.feature{top:14px;font-size:13px}
.feature h4{font-weight:400;font-size:13.5px;margin-bottom:9px}
.feature p{line-height:18px;width:195px}
.divider{top:20px;width:1px;height:72px;background:#9ec25a}
.social{left:650px;top:46px;display:flex;gap:14px}
.social .chip{display:flex;flex-direction:column;align-items:center;gap:3px;font-size:10px}
.social .sq{width:40px;height:36px;background:#cfcfcf;border-radius:5px;border:1px solid #eee}

.site-footer{left:0;top:993px;width:915px;height:180px;background:var(--footer)}
.col{top:21px;font-size:13px}
.col h5{font-weight:400;font-size:13.5px;color:#111;margin-bottom:29px}
.col a{display:block;color:var(--green);line-height:21px}
.pay{left:748px;top:54px;display:grid;grid-template-columns:58px 58px;gap:14px 12px}
.pay span{height:36px;border:1px solid #bbb;background:#fff;font:700 12px/34px "Arimo",sans-serif;text-align:center;color:#2a3a7a}
.legal{left:0;top:1173px;width:915px;height:27px;background:var(--legal);font-size:13px;padding:7px 0 0 60px;color:#111}
</style>
</head>
<body>

<header>
  <div class="abs brand">Tallowmark</div>
  <div class="abs account">
    <a href="#">Sign In</a><span>|</span>
    <a href="#"><svg width="14" height="12" viewBox="0 0 14 12"><path d="M0 1h2.5l2 7h7l1.5-5H4" fill="none" stroke="#6a9a1a" stroke-width="1.3"/><circle cx="5.5" cy="10.5" r="1.1" fill="#6a9a1a"/><circle cx="10.5" cy="10.5" r="1.1" fill="#6a9a1a"/></svg> Cart (0)</a>
  </div>
  <nav class="abs main-nav">
    <a href="#" style="width:82px">Home</a>
    <a href="#" style="width:79px">Signs<i class="caret"></i></a>
    <a href="#" style="width:103px">Banners<i class="caret"></i></a>
    <a href="#" style="width:111px">Lettering<i class="caret"></i></a>
    <a href="#" style="width:82px">Prints<i class="caret"></i></a>
    <a href="#">Gallery</a>
  </nav>
  <div class="abs search">Search</div>
  <div class="abs search-btn"><svg width="12" height="12" viewBox="0 0 12 12"><path d="M1 2l4 4-4 4M6 2l4 4-4 4" fill="none" stroke="#fff" stroke-width="1.8"/></svg></div>
</header>

<section class="abs hero">
  <div class="abs hero-glow"></div>
  <div class="abs hero-photo" role="img" aria-label="Bright interior room with a large leafy plant print hung on the wall"></div>
  <svg class="abs burst" width="143" height="122" viewBox="0 0 143 122">
    <polygon fill="#ffee00" points="18,0 143,0 143,122 131,106 120,118 112,100 97,110 92,92 76,98 76,80 58,80 64,64 44,58 56,44 36,34 54,26 38,12 58,10"/>
    <text x="90" y="66" text-anchor="middle" transform="rotate(-22 90 54)" font-family="Ubuntu,sans-serif" font-weight="500" font-size="36" fill="#111">-15%</text>
  </svg>
  <h1 class="abs hero-title"><span>Banner</span> Printing</h1>
  <div class="abs hero-step" style="top:96px">1) Upload your files</div>
  <a class="abs browse" href="#">Browse
    <svg width="26" height="24" viewBox="0 0 26 24"><rect x="1" y="4" width="24" height="19" rx="2" fill="#fff"/><path d="M13 18V9M9 12l4-4 4 4" fill="none" stroke="#6a9a1a" stroke-width="2.2"/></svg>
  </a>
  <div class="abs hero-step" style="top:203px">2) Select vinyl size</div>
  <div class="abs hero-step" style="top:241px">3) Order now online!</div>
  <div class="abs pager"><span>&lt;</span><span>1</span><span>2</span><span class="on">3</span><span>4</span><span>5</span><span>&gt;</span></div>
</section>

<main>
  <article class="abs card" style="left:44px">
    <h2>Signs</h2>
    <div class="thumb" role="img" aria-label="Green van parked in a grassy field under a blue sky beside a road sign" style="background:linear-gradient(180deg,#3f6fb0 0%,#9bb9d6 45%,#7f9a4e 70%,#5a7a28 100%)"></div>
    <h3>Excepturi sint occaecati cupiditate</h3>
    <p>non provident, similique sunt in culpa qui officia deserunt mollitia animi, id est laborum et dolorum fuga. non provident, similique sunt in culpa</p>
    <a class="read-more" href="#"><svg width="21" height="21" viewBox="0 0 21 21"><circle cx="10.5" cy="10.5" r="9" fill="#fff" stroke="#5a8612" stroke-width="2"/><path d="M8 6l6 4.5L8 15z" fill="#5a8612"/></svg>Read more</a>
  </article>
  <article class="abs card" style="left:324px">
    <h2>Banners</h2>
    <div class="thumb" role="img" aria-label="Wide-format printer producing a colourful banner" style="border:1px solid #666;background:linear-gradient(90deg,#fff 0%,#e8e8e8 25%,#3a3a3a 45%,#b04a2a 60%,#3a3a3a 80%,#fff 100%)"></div>
    <h3>Assumenda est, omnis dolor omnis</h3>
    <p>endus. Temporibus autem quibusdam quibusdam et aut officiis debitis aut rerum necessitatibus saepe eveniet endus. Temporibus autem quibusdam</p>
    <a class="read-more" href="#"><svg width="21" height="21" viewBox="0 0 21 21"><circle cx="10.5" cy="10.5" r="9" fill="#fff" stroke="#5a8612" stroke-width="2"/><path d="M8 6l6 4.5L8 15z" fill="#5a8612"/></svg>Read more</a>
  </article>
  <article class="abs card" style="left:606px">
    <h2>Lettering</h2>
    <div class="thumb" role="img" aria-label="Shop window with vinyl lettering quotes beside fresh green salad" style="background:linear-gradient(90deg,#e9ddd0 0%,#d8c6b2 35%,#6e9a3a 55%,#4c7a22 80%,#f07d10 92%)"></div>
    <h3>On the other hand, we denounce</h3>
    <p>righteous indignation and dislike men who are so beguiled and demoralized by the charms of pleasure of the righteous indignation and dislike men</p>
    <a class="read-more" href="#"><svg width="21" height="21" viewBox="0 0 21 21"><circle cx="10.5" cy="10.5" r="9" fill="#fff" stroke="#5a8612" stroke-width="2"/><path d="M8 6l6 4.5L8 15z" fill="#5a8612"/></svg>Read more</a>
  </article>
</main>

<section class="abs features">
  <div class="abs feature" style="left:60px">
    <h4>24 hours printing</h4>
    <p>Sed lacinia, nibh in tempus porttitor, nisi elit viverra libero, in cursus eros nisi quis</p>
  </div>
  <svg class="abs" style="left:251px;top:32px" width="48" height="48" viewBox="0 0 48 48"><circle cx="24" cy="24" r="21" fill="#fff" stroke="#444" stroke-width="2"/><path d="M24 10v14l8 6" fill="none" stroke="#222" stroke-width="2"/></svg>
  <div class="abs divider" style="left:317px"></div>
  <div class="abs feature" style="left:337px">
    <h4>Quality</h4>
    <p>Maecenas ut metus libero, ut hendrerit leo. In mattis facilisis metus, ut malesuada</p>
  </div>
  <svg class="abs" style="left:529px;top:31px" width="48" height="48" viewBox="0 0 48 48"><circle cx="24" cy="24" r="22" fill="#f2f2f2" stroke="#ccc" stroke-width="2"/><circle cx="24" cy="24" r="15" fill="none" stroke="#bbb" stroke-width="1.5"/></svg>
  <div class="abs divider" style="left:598px"></div>
  <div class="abs feature" style="left:623px"><h4>Follow Us</h4></div>
  <div class="abs social">
    <a class="chip" href="#"><span class="sq"></span>Friendwall</a>
    <a class="chip" href="#"><span class="sq"></span>Chirpline</a>
    <a class="chip" href="#"><svg width="42" height="38" viewBox="0 0 42 38"><rect x="1" y="1" width="40" height="36" rx="5" fill="#e6e6e6" stroke="#999"/><rect x="8" y="10" width="26" height="18" fill="#fff" stroke="#333" stroke-width="1.6"/><path d="M8 10l13 10 13-10" fill="none" stroke="#333" stroke-width="1.6"/></svg>Email</a>
  </div>
</section>

<footer class="abs site-footer">
  <div class="abs col" style="left:60px"><h5>Products</h5><a href="#">Signs</a><a href="#">Banners</a><a href="#">Lettering</a><a href="#">Prints</a></div>
  <div class="abs col" style="left:216px"><h5>About Us</h5><a href="#">Why choose Us?</a><a href="#">Who we are?</a><a href="#">Career</a></div>
  <div class="abs col" style="left:420px"><h5>Contact Us</h5><a href="#">Contact Us</a><a href="#">Blog</a><a href="#">Newsletter</a><a href="#">Friendwall</a><a href="#">Chirpline</a></div>
  <div class="abs col" style="left:590px"><h5>Language</h5><a href="#">English</a><a href="#">Deutsch</a><a href="#">Español</a><a href="#">Italiano</a></div>
  <div class="abs col" style="left:752px"><h5>We accept</h5></div>
  <div class="abs pay"><span>PayLoop</span><span>Vantra</span><span>Mintcard</span><span>Roamcard</span></div>
</footer>
<div class="abs legal">2012 © Shipping and Returning Policy</div>

</body>
</html>
```